Bref créative
Halden Byte Solutions - Stationery
Business Cards, Letter Head & Envelopes
Professional
Gordon Pelley
President
379 Cobble Lane Suite 4150
Sudbury, MA 01776
gpelley@halden-byte.com
www.halden-byte.com

```html
<!DOCTYPE html>
<html lang="en">
<head>
<meta charset="utf-8">
<title>Halden Byte Solutions – Stationery</title>
<link href="https://fonts.googleapis.com/css2?family=Arimo:wght@400;700&display=swap" rel="stylesheet">
<style>
:root{
  --bg:#8a8a8a;
  --paper:#ffffff;
  --red-dark:#6e0f06;
  --red:#b3260f;
  --ink:#333333;
  --muted:#8c8c8c;
  --charcoal:#1c1c1c;
}
*{margin:0;padding:0;box-sizing:border-box}
html,body{width:1200px;height:281px;overflow:hidden}
body{background:var(--bg);font-family:"Arimo",Arial,sans-serif;position:relative;color:var(--ink)}
.piece{position:absolute;background:var(--paper);box-shadow:0 2px 5px rgba(0,0,0,.35);overflow:hidden}
.piece svg.swoosh{position:absolute;left:0;top:0;width:100%}
.brand{position:absolute;display:flex;align-items:center;gap:3px;font-weight:700;white-space:nowrap}
.brand i{display:block;background:var(--red)}
.brand.on-red{color:#fff}
.brand.on-red i{background:#fff}
.brand.on-white{color:var(--red)}
.details{position:absolute;font-size:3.6px;line-height:1.45;color:var(--muted)}
.details b{color:var(--ink);font-size:4.4px}
.footer{position:absolute;left:0;right:0;text-align:center;font-size:3.4px;color:var(--muted)}
.card-red{background:linear-gradient(135deg,var(--red),var(--red-dark))}
.card-dark{background:var(--charcoal)}
.flap{background:var(--charcoal)}
</style>
</head>
<body>

<!-- Business card fronts -->
<div class="piece" style="left:12px;top:42px;width:96px;height:54px">
  <div class="brand on-white" style="left:10px;top:20px;font-size:7px"><i style="width:7px;height:7px"></i>Halden Byte Solutions</div>
</div>

<div class="piece" style="left:12px;top:104px;width:80px;height:46px">
  <div class="brand on-white" style="left:6px;top:5px;font-size:4.6px"><i style="width:4px;height:4px"></i>Halden Byte Solutions</div>
  <div class="details" style="left:6px;top:16px"><b>Gordon Pelley</b><br>President<br>379 Cobble Lane Suite 4150<br>Sudbury, MA 01776</div>
</div>

<div class="piece" style="left:100px;top:104px;width:80px;height:46px">
  <svg class="swoosh" viewBox="0 0 80 46" height="46" preserveAspectRatio="none"><path d="M0 30 Q40 18 80 34 L80 46 L0 46Z" fill="#b3260f"/></svg>
  <div class="brand on-white" style="left:8px;top:10px;font-size:5.4px"><i style="width:5px;height:5px"></i>Halden Byte Solutions</div>
</div>

<!-- Business card variations -->
<div class="piece" style="left:12px;top:188px;width:86px;height:48px">
  <svg class="swoosh" viewBox="0 0 86 48" height="48" preserveAspectRatio="none"><path d="M0 34 Q43 20 86 36 L86 48 L0 48Z" fill="#b3260f"/></svg>
  <div class="brand on-white" style="left:10px;top:12px;font-size:5.6px"><i style="width:5px;height:5px"></i>Halden Byte Solutions</div>
</div>
<div class="piece card-red" style="left:106px;top:188px;width:86px;height:48px">
  <div class="brand on-red" style="left:10px;top:20px;font-size:5.6px"><i style="width:5px;height:5px"></i>Halden Byte Solutions</div>
</div>
<div class="piece card-dark" style="left:200px;top:188px;width:76px;height:48px">
  <div class="brand on-red" style="left:7px;top:20px;font-size:5px"><i style="width:5px;height:5px"></i>Halden Byte Solutions</div>
</div>

<!-- Letterheads -->
<div class="piece letterhead" style="left:288px;top:20px;width:130px;height:232px">
  <svg class="swoosh" viewBox="0 0 130 44" height="44" preserveAspectRatio="none"><defs><linearGradient id="lh1" x1="0" x2="1"><stop offset="0" stop-color="#6e0f06"/><stop offset="1" stop-color="#b3260f"/></linearGradient></defs><path d="M0 0 H130 V28 Q70 46 0 34Z" fill="url(#lh1)"/><path d="M0 37 Q70 49 130 31" stroke="#b3260f" stroke-width="1" fill="none"/></svg>
  <div class="brand on-red" style="left:10px;top:10px;font-size:5.4px"><i style="width:5px;height:5px"></i>Halden Byte Solutions</div>
  <div class="footer" style="bottom:8px">379 Cobble Lane Suite 4150 · Sudbury, MA 01776<br>gpelley@halden-byte.com · www.halden-byte.com</div>
</div>

<div class="piece letterhead" style="left:548px;top:20px;width:130px;height:232px">
  <svg class="swoosh" viewBox="0 0 130 44" height="44" preserveAspectRatio="none"><defs><linearGradient id="lh2" x1="0" x2="1"><stop offset="0" stop-color="#6e0f06"/><stop offset="1" stop-color="#b3260f"/></linearGradient></defs><path d="M0 0 H130 V28 Q70 46 0 34Z" fill="url(#lh2)"/><path d="M0 37 Q70 49 130 31" stroke="#b3260f" stroke-width="1" fill="none"/></svg>
  <div class="brand on-red" style="left:10px;top:10px;font-size:5.4px"><i style="width:5px;height:5px"></i>Halden Byte Solutions</div>
  <div class="footer" style="bottom:8px">379 Cobble Lane Suite 4150 · Sudbury, MA 01776<br>gpelley@halden-byte.com · www.halden-byte.com</div>
</div>

<!-- Compliment slips -->
<div class="piece slip" style="left:684px;top:20px;width:168px;height:96px">
  <svg class="swoosh" viewBox="0 0 168 30" height="30" preserveAspectRatio="none"><path d="M0 0 H168 V18 Q90 32 0 24Z" fill="#9c1e0c"/></svg>
  <div class="brand on-red" style="left:10px;top:7px;font-size:5px"><i style="width:5px;height:5px"></i>Halden Byte Solutions</div>
  <div class="footer" style="bottom:6px">379 Cobble Lane Suite 4150 · Sudbury, MA 01776</div>
</div>
<div class="piece slip" style="left:684px;top:148px;width:168px;height:96px">
  <svg class="swoosh" viewBox="0 0 168 30" height="30" preserveAspectRatio="none"><path d="M0 0 H168 V18 Q90 32 0 24Z" fill="#9c1e0c"/></svg>
  <div class="brand on-red" style="left:10px;top:7px;font-size:5px"><i style="width:5px;height:5px"></i>Halden Byte Solutions</div>
  <div class="footer" style="bottom:6px">379 Cobble Lane Suite 4150 · Sudbury, MA 01776</div>
</div>

<!-- Envelopes -->
<div class="piece flap" style="left:972px;top:22px;width:180px;height:62px">
  <svg class="swoosh" viewBox="0 0 180 62" height="62" preserveAspectRatio="none"><path d="M0 0 L90 40 L180 0" stroke="#444" stroke-width="1" fill="none"/></svg>
  <div class="brand on-red" style="left:62px;top:44px;font-size:5px"><i style="width:5px;height:5px"></i>Halden Byte Solutions</div>
</div>
<div class="piece envelope" style="left:972px;top:78px;width:180px;height:80px">
  <svg class="swoosh" viewBox="0 0 180 80" height="80" preserveAspectRatio="none"><path d="M0 0 L90 44 L180 0" stroke="#d6d6d6" stroke-width="1" fill="none"/></svg>
</div>
<div class="piece envelope" style="left:962px;top:156px;width:205px;height:100px">
  <svg class="swoosh" viewBox="0 0 205 100" height="100" preserveAspectRatio="none"><path d="M0 0 L102 48 L205 0" stroke="#d6d6d6" stroke-width="1" fill="none"/></svg>
  <div class="brand on-white" style="left:8px;top:8px;font-size:4.6px"><i style="width:4px;height:4px"></i>Halden Byte Solutions</div>
</div>

</body>
</html>
```